New Business Card Design Project

I would like my card design to look exactly like the logo, design, layout, and print of the current attached file. The only change I would like made would be for the print to say THE KMW GROUP instead of THE HALLORAN GROUP. Basically, just replace his group name with my group name. I would also like the backgroud to be the same texture and color as the attached file. I love the dark blue lettering and house logo on the card.

I am completely open to the rest of the card design. I just want something clean and simple. Only basic contact info required on the card. Maybe just name: Kyle M Warrick and cell # 555.914.2087 and email kyle@orchidhomesagent.com

```html
<!DOCTYPE html>
<html lang="en">
<head>
<meta charset="utf-8">
<title>The KMW Group — Business Card</title>
<link rel="stylesheet" href="https://fonts.googleapis.com/css2?family=Montserrat:wght@400;500&family=Open+Sans:wght@400;600&family=Arimo:wght@700&display=swap">
<style>
  :root {
    --backdrop: #e2e2e2;
    --card-silver-light: #c4c4c4;
    --card-silver-dark: #a9a9a9;
    --ink-navy: #131530;
    --card-navy: #0e0f26;
    --pattern-navy: #1b1d36;
    --paper-white: #e9e9ec;
  }
  * { margin: 0; padding: 0; box-sizing: border-box; }
  html, body { width: 1200px; height: 802px; overflow: hidden; }
  body { background: var(--backdrop); position: relative; }

  .card {
    position: absolute;
    top: 274px;
    width: 443px;
    height: 265px;
    box-shadow: 2px 3px 5px rgba(0,0,0,0.35);
  }

  /* Front */
  .card-front {
    left: 136px;
    background:
      radial-gradient(ellipse at 30% 20%, rgba(255,255,255,0.18), transparent 60%),
      linear-gradient(135deg, var(--card-silver-light), var(--card-silver-dark));
  }
  .brand-square {
    position: absolute;
    left: 80px;
    top: 56px;
    width: 98px;
    height: 98px;
    background: var(--ink-navy);
  }
  .brand-divider {
    position: absolute;
    left: 213px;
    top: 44px;
    width: 1.5px;
    height: 125px;
    background: var(--ink-navy);
  }
  .brand-name {
    position: absolute;
    left: 232px;
    top: 58px;
    font-family: "Montserrat", sans-serif;
    font-weight: 400;
    font-size: 31px;
    line-height: 34px;
    letter-spacing: 4px;
    color: var(--ink-navy);
  }
  .brand-name span { display: block; }
  .contact-name {
    position: absolute;
    left: 0;
    width: 100%;
    top: 197px;
    text-align: center;
    font-family: "Arimo", sans-serif;
    font-weight: 700;
    font-size: 15px;
    letter-spacing: 0.3px;
    color: var(--ink-navy);
  }
  .contact-line {
    position: absolute;
    left: 0;
    width: 100%;
    top: 225px;
    text-align: center;
    font-family: "Open Sans", sans-serif;
    font-size: 12.5px;
    color: var(--ink-navy);
  }
  .contact-line b { font-weight: 600; }
  .contact-line .sep { margin: 0 6px; }

  /* Back */
  .card-back {
    left: 624px;
    background: var(--card-navy);
    overflow: hidden;
  }
  .back-pattern {
    position: absolute;
    inset: 0;
    background: linear-gradient(180deg, var(--pattern-navy), var(--card-navy) 140%);
    opacity: 0.7;
  }
  .back-name {
    position: absolute;
    left: 0;
    width: 100%;
    top: 119px;
    text-align: center;
    font-family: "Montserrat", sans-serif;
    font-weight: 500;
    font-size: 24px;
    line-height: 28px;
    letter-spacing: 3px;
    color: var(--paper-white);
  }
</style>
</head>
<body>
  <section class="card card-front">
    <div class="brand-square"></div>
    <div class="brand-divider"></div>
    <h1 class="brand-name"><span>THE</span><span>KMW</span><span>GROUP</span></h1>
    <p class="contact-name">KYLE M WARRICK</p>
    <p class="contact-line"><b>M:</b> 555.914.2087<span class="sep">|</span><b>E:</b> kyle@orchidhomesagent.com</p>
  </section>

  <section class="card card-back">
    <div class="back-pattern" role="img" aria-label="Repeating tone-on-tone brand pattern on navy"></div>
    <p class="back-name">KMW</p>
  </section>
</body>
</html>
```